BRISKWATER MOTION GYM FLYER DESIGN

We want a flyer designed for our gym. We have an example of a flyer which we like and I have put it into the images I have uploaded. I would like to recreate using our pictures, so its a pretty straight forward job. We also want to put our weekly timetable on the back of the flyer. We would like the size of the flyer to be A5.

Target Market(s)

FITNESS

Industry/Entity Type

Gym

Colors
33a6d7
ffffff

Requirements
Must have
• We just want to recreate the flyer but we must have the following info on the flyer and we want our timetable on the back of the flyer which you can get from this link: http://www.briskwatermotiongym.com/timetable
• Briskwater Motion Gym is a fun community of humble people. Our goal is to help guide you towards a fitter, healthier lifestyle!
• Our Programs
• HIIT
• High intensity interval training is 30-45 minutes of fat burning fun. The class is a mix of cardio, bodyweight and some resistance movements.
• Conditioning
• A full hour of strength, cardio and bodyweight training to get you in tip top shape. Expect a mix of barbells, kettlebells, rowing machines, bikes and other training methods.
• KPL
• This is our big Friday session to set you up for the weekend. 90 minutes of hard training that is done with a team emphasis. From heavy lifting to cardio triathlons, this class has it all but not for the faint hearted.
• Muay Thai
• Commonly known as the science of 8 limbs you will learn how to punch, kick, knee and elbow. Thailands national sport is a great way to get your fitness kick. We train the complete beginner all the way to international fighters so you are in great hands.
• Kids Muay Thai
• Our junior program starts from age 6 onwards. Muay Thai is a great way for kids to get active and fit while learning new skills. Training in martial arts also teaches self discipline and socialisation skills.
• Yoga
• A combination of physical and mental practises that will leave you focused and refreshed for whatever the week throws at you. We always recommend our yoga classes as a great way to balance the high intensity training we offer.
• U-Press
• Strength training with a little bit of conditioning. We regularly update the program and re test lifts to ensure you are making progress and getting stronger.
• CONTACT US
• OUR LOCATION:
• Unit 42C
• 273 Quillan Street
• Fenwick Hollow
• Glasgow
• G72TR
• Phone: 07950362814
• Email: info@briskwatermotiongym.com
• Web: www.briskwatermotiongym.com
Nice to have
• Can use all the picture but if not be good to use the boxing one and the group training one.

```html
<!DOCTYPE html>
<html lang="en">
<head>
<meta charset="utf-8">
<title>Briskwater Motion Gym – Weekly Timetable</title>
<link href="https://fonts.googleapis.com/css2?family=Oswald:wght@400;500&family=Roboto+Condensed:wght@400;700&display=swap" rel="stylesheet">
<style>
  :root {
    --brand-blue: #33a6d7;
    --page-blue: #1f98d3;
    --row-grey: #e3e4e5;
    --ink: #1d2b4f;
    --white: #ffffff;
    --photo-dark: #3b4148;
    --photo-mid: #6d6a66;
  }
  * { margin: 0; padding: 0; box-sizing: border-box; }
  html, body { width: 1200px; height: 855px; overflow: hidden; background: var(--white); }
  .flyer {
    position: relative;
    width: 1200px; height: 855px;
    background: var(--page-blue);
    font-family: "Roboto Condensed", sans-serif;
    overflow: hidden;
  }
  .hero-photo {
    position: absolute; left: 0; top: 0; width: 797px; height: 192px;
    background: linear-gradient(100deg, var(--photo-dark) 0%, #7d7c78 45%, #c9c6bf 70%, var(--photo-mid) 100%);
    clip-path: polygon(0 0, 100% 0, 100% 80%, 0 100%);
  }
  .side-panel {
    position: absolute; left: 797px; top: 0; width: 403px; height: 855px;
    background: var(--page-blue);
  }
  .side-photo {
    position: absolute; left: 0; top: 0; width: 403px; height: 532px;
    background: linear-gradient(160deg, #8a8d8f 0%, #4a4f55 40%, #2f3337 75%, #5a5d60 100%);
    clip-path: polygon(0 0, 100% 0, 100% 100%, 0 93%);
  }
  .brand {
    position: absolute; left: 0; top: 632px; width: 403px;
    display: flex; align-items: center; justify-content: center; gap: 12px;
    color: var(--white);
    font-family: "Oswald", sans-serif; font-weight: 500; font-size: 27px; letter-spacing: 1px;
  }
  .brand-dot { width: 14px; height: 14px; border-radius: 50%; background: var(--white); }
  .address {
    position: absolute; left: 0; top: 784px; width: 403px; text-align: center;
    color: var(--white); font-size: 11.5px; font-weight: 700;
  }
  .site {
    position: absolute; left: 0; top: 806px; width: 403px; text-align: center;
    color: var(--white); font-size: 18px;
  }
  .schedule { position: absolute; left: 22px; top: 196px; width: 754px; }
  .week-row { display: flex; gap: 9px; }
  .week-row + .week-row { margin-top: 20px; }
  .day-card { width: 245px; background: var(--white); }
  .day-name {
    height: 33px; padding: 2px 8px 0;
    background: var(--brand-blue); color: var(--white);
    font-family: "Oswald", sans-serif; font-size: 21px; line-height: 31px;
    border-bottom: 2px solid var(--white);
  }
  .session {
    display: flex; height: 21px; margin-top: 1px;
    background: var(--row-grey); color: var(--ink);
    font-size: 13.5px; line-height: 21px;
  }
  .session-time { width: 57px; padding-left: 8px; }
  .contact-bar {
    position: absolute; left: 22px; top: 793px; width: 754px;
    border-top: 1px solid rgba(255,255,255,0.8);
    display: flex; align-items: center; height: 52px;
    color: var(--white); font-size: 13px;
  }
  .contact-title { font-family: "Oswald", sans-serif; font-weight: 500; font-size: 17px; width: 135px; padding-left: 3px; }
  .contact-phone { width: 112px; }
  .divider { width: 35px; text-align: left; }
  .contact-email { width: 223px; }
</style>
</head>
<body>
<div class="flyer">
  <div class="hero-photo" role="img" aria-label="Photo of an athlete swinging a kettlebell in the gym"></div>

  <div class="schedule">
    <div class="week-row">
      <section class="day-card">
        <h2 class="day-name">MONDAY</h2>
        <div class="session"><span class="session-time">07:00</span><span>Conditioning</span></div>
        <div class="session"><span class="session-time">08:00</span><span>Open Gym</span></div>
        <div class="session"><span class="session-time">10:00</span><span>U-Press</span></div>
        <div class="session"><span class="session-time">12:10</span><span>Lunch time HIIT</span></div>
        <div class="session"><span class="session-time">16:00</span><span>Open Gym</span></div>
        <div class="session"><span class="session-time">17:00</span><span>U-Press</span></div>
        <div class="session"><span class="session-time">18:00</span><span>Fundamentals</span></div>
        <div class="session"><span class="session-time">18:00</span><span>Muay Thai Foundations</span></div>
        <div class="session"><span class="session-time">19:00</span><span>Strength and Conditioning</span></div>
        <div class="session"></div>
        <div class="session"></div>
      </section>
      <section class="day-card">
        <h2 class="day-name">TUESDAY</h2>
        <div class="session"><span class="session-time">06:00</span><span>U-Press</span></div>
        <div class="session"><span class="session-time">07:00</span><span>Fight Camp Muay Thai</span></div>
        <div class="session"><span class="session-time">08:00</span><span>Open Gym</span></div>
        <div class="session"><span class="session-time">12:10</span><span>Lunch time HIIT</span></div>
        <div class="session"><span class="session-time">16:00</span><span>Open Gym</span></div>
        <div class="session"><span class="session-time">17:15</span><span>HIIT</span></div>
        <div class="session"><span class="session-time">18:00</span><span>Conditioning</span></div>
        <div class="session"><span class="session-time">18:00</span><span>Kids</span></div>
        <div class="session"><span class="session-time">19:00</span><span>Muay Thai Intermediate</span></div>
        <div class="session"></div>
        <div class="session"></div>
      </section>
      <section class="day-card">
        <h2 class="day-name">WEDNESDAY</h2>
        <div class="session"><span class="session-time">06:00</span><span>Strength and Conditioning</span></div>
        <div class="session"><span class="session-time">07:00</span><span>Yoga</span></div>
        <div class="session"><span class="session-time">08:00</span><span>Open Gym</span></div>
        <div class="session"><span class="session-time">10:00</span><span>U-Press</span></div>
        <div class="session"><span class="session-time">16:00</span><span>Open Gym</span></div>
        <div class="session"><span class="session-time">17:00</span><span>U-Press</span></div>
        <div class="session"><span class="session-time">17:15</span><span>HIIT</span></div>
        <div class="session"><span class="session-time">18:00</span><span>Fundamentals</span></div>
        <div class="session"><span class="session-time">18:00</span><span>Muay Thai Foundations</span></div>
        <div class="session"><span class="session-time">19:15</span><span>Yoga</span></div>
        <div class="session"></div>
      </section>
    </div>
    <div class="week-row">
      <section class="day-card">
        <h2 class="day-name">THURSDAY</h2>
        <div class="session"><span class="session-time">07:00</span><span>Conditioning</span></div>
        <div class="session"><span class="session-time">08:00</span><span>Open Gym</span></div>
        <div class="session"><span class="session-time">12:10</span><span>Lunch time HIIT</span></div>
        <div class="session"><span class="session-time">16:00</span><span>Open Gym</span></div>
        <div class="session"><span class="session-time">17:15</span><span>HIIT (6/30)</span></div>
        <div class="session"><span class="session-time">18:00</span><span>Conditioning</span></div>
        <div class="session"><span class="session-time">18:00</span><span>Kids</span></div>
        <div class="session"><span class="session-time">19:00</span><span>Muay Thai Intermediate</span></div>
        <div class="session"></div>
        <div class="session"></div>
        <div class="session"></div>
      </section>
      <section class="day-card">
        <h2 class="day-name">FRIDAY</h2>
        <div class="session"><span class="session-time">06:00</span><span>U-Press</span></div>
        <div class="session"><span class="session-time">07:00</span><span>Fight Camp Muay Thai</span></div>
        <div class="session"><span class="session-time">08:00</span><span>Open Gym</span></div>
        <div class="session"><span class="session-time">10:00</span><span>U-Press</span></div>
        <div class="session"><span class="session-time">12:10</span><span>Lunch time HIIT</span></div>
        <div class="session"><span class="session-time">16:00</span><span>Open Gym</span></div>
        <div class="session"><span class="session-time">17:00</span><span>U-Press</span></div>
        <div class="session"><span class="session-time">18:00</span><span>KPL</span></div>
        <div class="session"></div>
        <div class="session"></div>
        <div class="session"></div>
      </section>
      <section class="day-card">
        <h2 class="day-name">SATURDAY</h2>
        <div class="session"><span class="session-time">10:00</span><span>Saturday Circuit</span></div>
        <div class="session"><span class="session-time">11:00</span><span>Open Gym</span></div>
        <div class="session"><span class="session-time">11:00</span><span>Fundamentals</span></div>
        <div class="session"><span class="session-time">11:00</span><span>Kids</span></div>
        <div class="session"><span class="session-time">12:00</span><span>Muay Thai Foundations</span></div>
        <div class="session"></div>
        <div class="session"></div>
        <div class="session"></div>
        <div class="session"></div>
        <div class="session"></div>
        <div class="session"></div>
      </section>
    </div>
  </div>

  <footer class="contact-bar">
    <span class="contact-title">CONTACT US:</span>
    <span class="contact-phone">07950362814</span>
    <span class="divider">|</span>
    <span class="contact-email">info@briskwatermotiongym.com</span>
    <span class="divider">|</span>
    <span class="contact-web">www.briskwatermotiongym.com</span>
  </footer>

  <aside class="side-panel">
    <div class="side-photo" role="img" aria-label="Photo of a woman training on a rowing machine with a group in the gym"></div>
    <div class="brand"><span class="brand-dot"></span><span>BRISKWATER MOTION GYM</span></div>
    <p class="address">Unit 42C 273 Quillan Street Fenwick Hollow Glasgow G72TR</p>
    <p class="site">www.briskwatermotiongym.com</p>
  </aside>
</div>
</body>
</html>
```